Website Design for Quarry Sun inc

I want eye candy on opening page.  Prefer yellows, greens and orange to darker colors.  This contest will be won on the home page, then we together will use that theme for the rest of the site (about 8 pages total, NO shopping cart).  My current site is www.BrindleRaySolar.com, you can use as much or as little of the content, photos, etc as you want.  I am Carl Dunmore - general partner.  The following web sites are ones that I like parts of, and would love an amalgm of them, based on my comments.  GOOD LUCK!

http://www.solarhaven.example/   -  The largest, most talked about company in the business, and a great site, probably my favorite.

 

 

http://www.tulmasolar.example/  -  Clean and clear

 

http://www.thebrightpowerhouse.example/index.html   -  Just for the pic of plug lit by sun

http://www.kestrel-solar.example/   -  Really like the general look of the site

 

http://www.solarloom.example/index.html  -  Good Flash sequence

 

http://www.dulasolar.example/cm/Home.html  -  Most offices in the business - not bad site

I don't know what a vector file is.  I have an AI file, does that work?  Meanwhile, I can't find how to upload it into my brief.  Advise.

Target Market(s)

NOT TREEHUGGERS!  Homeowners.  Retirees.  Early adopters.  OK, maybe a treehugger or two.  

Industry/Entity Type

Solar

Requirements
Must have
• Logo.  Any pics must be mine.  If you need more pics, email me.  Ease of use, compelling. 
Nice to have
• In California, Arizona and Nevada, and coming to a city near YOU!!

```html
<!DOCTYPE html>
<html lang="en">
<head>
<meta charset="utf-8">
<title>Quarry Sun inc — Go Solar Now</title>
<link rel="stylesheet" href="https://fonts.googleapis.com/css2?family=Didact+Gothic&family=Open+Sans:wght@400;600&display=swap">
<style>
:root{
  --green:#45a82e;
  --green-dark:#2f8a1f;
  --green-text:#5aa82a;
  --orange:#f7941d;
  --orange-dark:#e07b0c;
  --orange-text:#f5a00f;
  --ink:#222;
  --grey:#555;
  --grey-light:#888;
  --panel:#f4f4f4;
  --shadow:#6b6b6b;
}
*{margin:0;padding:0;box-sizing:border-box}
html,body{width:1200px;height:908px;overflow:hidden}
body{
  position:relative;
  background:linear-gradient(#e9e9e9 0,#fff 140px,#fff 100%);
  font-family:"Open Sans",sans-serif;color:var(--ink);
}
.page{position:absolute;left:111px;top:0;width:984px;height:908px}
.header{position:absolute;left:0;top:0;width:984px;height:146px;background:#fff}
.brand{position:absolute;left:36px;top:32px;display:flex;align-items:center;gap:14px}
.brand-mark{width:62px;height:62px;border-radius:50%;background:#f6b51c}
.brand-name{font-family:"Didact Gothic",sans-serif;font-size:40px;color:#555;letter-spacing:.5px}
.contact{position:absolute;top:40px;font-family:"Didact Gothic",sans-serif;font-size:17px;color:#444}
.contact.sb{left:470px}.contact.fr{left:745px}
.nav{position:absolute;left:454px;top:90px;display:flex;gap:2px}
.nav a{
  display:block;width:120px;height:57px;line-height:58px;text-align:center;
  background:linear-gradient(#6cc14a,var(--green) 55%,#38961f);
  border-radius:10px 10px 0 0;color:#fff;text-decoration:none;
  font-family:"Didact Gothic",sans-serif;font-size:13px;letter-spacing:.5px;
}
.nav a:first-child{width:115px}
.rule{position:absolute;left:0;top:144px;width:984px;height:3px;background:var(--green)}
.hero{position:absolute;left:0;top:147px;width:984px;height:249px;background:#fff}
.hero-photo{
  position:absolute;left:0;top:0;width:660px;height:249px;
  background:linear-gradient(90deg,#5b8f4a 0,#c98a6a 30%,#e8e4dc 55%,#c9dbe6 78%,rgba(255,255,255,0) 100%);
}
.hero-copy{position:absolute;right:30px;top:62px;text-align:center;width:320px}
.hero-kicker{font-family:"Didact Gothic",sans-serif;font-size:31px;color:var(--orange)}
.hero-title{font-family:"Didact Gothic",sans-serif;font-size:33px;color:#111;margin-top:-4px}
.hero-sub{font-family:"Didact Gothic",sans-serif;font-size:18px;color:#555;margin-top:4px}
.btn{
  display:inline-block;background:linear-gradient(#fbab3a,var(--orange-dark));
  color:#fff;font-family:"Didact Gothic",sans-serif;text-decoration:none;
  box-shadow:0 1px 2px rgba(0,0,0,.4);
}
.btn-learn{position:absolute;left:765px;top:185px;width:167px;height:32px;line-height:33px;font-size:14px;text-align:center}
.benefits{
  position:absolute;left:0;top:397px;width:984px;height:218px;
  background:linear-gradient(#fff,var(--panel));
  border-bottom:5px solid var(--shadow);border-radius:0 0 26px 26px;
  box-shadow:0 3px 4px rgba(0,0,0,.25);
}
.benefit{position:absolute;top:0;height:210px;width:492px}
.benefit.residential{left:0}
.benefit.commercial{left:500px;border-left:1px solid #ccc}
.benefit h2{position:absolute;top:6px;font-family:"Didact Gothic",sans-serif;font-weight:400;font-size:18px;color:var(--orange-text)}
.residential h2{left:10px}.commercial h2{right:18px}
.benefit-icon{position:absolute;width:74px;height:74px;border-radius:12px}
.residential .benefit-icon{left:12px;top:75px;background:radial-gradient(#f4e640,#8bc34a 50%,#1e9fd8 80%)}
.commercial .benefit-icon{left:5px;top:65px;width:90px;height:90px;border-radius:50%;background:radial-gradient(circle at 40% 35%,#a9dde0,#2f8a95 70%,#1f5c66)}
.benefit-list{position:absolute;top:35px;list-style:none;font-family:"Open Sans",sans-serif;font-size:14.5px;line-height:17.5px;color:#333}
.residential .benefit-list{left:100px}.commercial .benefit-list{left:100px}
.benefit-list .lead{color:var(--green-text);font-size:14.5px}
.benefit-list li:not(.lead)::before{content:"* "}
.more{position:absolute;bottom:10px;font-size:14.5px;color:var(--green-text);display:flex;align-items:center;gap:6px}
.residential .more{left:162px}.commercial .more{left:192px}
.btn-more{width:110px;height:23px;line-height:23px;font-size:14px;text-align:center}
.cards{position:absolute;left:0;top:645px;width:984px;height:180px}
.card{
  position:absolute;top:50px;height:130px;
  background:linear-gradient(#fff 40%,#eaeaea);
  border-bottom:3px solid #777;border-radius:0 0 14px 14px;
  box-shadow:0 2px 3px rgba(0,0,0,.2);
}
.card.left{left:9px;width:305px}.card.mid{left:346px;width:305px}.card.right{left:670px;width:305px}
.card-photo{
  position:absolute;top:-48px;left:43px;width:218px;height:168px;border-radius:8px;
  background:linear-gradient(#2e86c8 0,#52a6d8 35%,#e8e9e4 50%,#5f8a3c 70%,#8a8a4a 100%);
  box-shadow:0 1px 3px rgba(0,0,0,.3);
}
.start-mark{position:absolute;left:96px;top:-40px;width:108px;height:108px;border-radius:50%;background:#f6b51c}
.start-title{position:absolute;left:0;top:72px;width:100%;text-align:center;font-family:"Didact Gothic",sans-serif;font-size:31px;color:#111}
.start-link{position:absolute;left:0;top:107px;width:100%;text-align:center;font-size:10px;color:var(--orange)}
.footer{position:absolute;left:22px;top:869px;font-size:14.5px;color:var(--grey-light);font-family:"Open Sans",sans-serif}
.footer nav{display:inline;margin-left:4px;color:#333}
.footer nav a{color:#333;text-decoration:none}
</style>
</head>
<body>
<div class="page">
  <header class="header">
    <div class="brand">
      <span class="brand-mark"></span>
      <span class="brand-name">Quarry Sun inc</span>
    </div>
    <div class="contact sb">Santa Barbara -(805)555-0142</div>
    <div class="contact fr">Fresno- (559) 555-0187</div>
    <nav class="nav">
      <a href="#">HOME</a><a href="#">PRODUCTS</a><a href="#">EMPLOYMENT</a><a href="#">CONTACT US</a>
    </nav>
    <div class="rule"></div>
  </header>

  <section class="hero">
    <div class="hero-photo" role="img" aria-label="Photo of a white Mediterranean-style home with solar panels on a terracotta roof, surrounded by palm trees"></div>
    <div class="hero-copy">
      <div class="hero-kicker">Go Solar Now!</div>
      <div class="hero-title">Saving you money</div>
      <div class="hero-sub">while saving the planet since 1983</div>
    </div>
    <a class="btn btn-learn" href="#">LEARN MORE</a>
  </section>

  <section class="benefits">
    <div class="benefit residential">
      <h2>RESIDENTIAL SOLAR</h2>
      <div class="benefit-icon" role="img" aria-label="Sun illustration icon"></div>
      <ul class="benefit-list">
        <li class="lead">Benefits of Residential Solar Power</li>
        <li>Save money</li>
        <li>Tax credits</li>
        <li>Appreciation</li>
        <li>Stabilize utility costs/stop inflation</li>
        <li>Help reduce our dependency on foreign energy</li>
        <li>Reduce green house gases</li>
        <li>Independence from VP&amp;L</li>
      </ul>
      <div class="more">for more information <a class="btn btn-more" href="#">Click here</a></div>
    </div>
    <div class="benefit commercial">
      <h2>COMMERCIAL SOLAR</h2>
      <div class="benefit-icon" role="img" aria-label="Ringed planet illustration icon"></div>
      <ul class="benefit-list">
        <li class="lead">Benefits of Commercial Solar Panels</li>
        <li>Save money</li>
        <li>30 percent unlimited federal tax credits</li>
        <li>Accelerated depreciation allowed</li>
        <li>Stabilize utility costs/stop inflation</li>
        <li>Help reduce our dependency on foreign energy</li>
        <li>Reduce green house gases</li>
        <li>Independence from VP&amp;L</li>
      </ul>
      <div class="more">for more information <a class="btn btn-more" href="#">Click here</a></div>
    </div>
  </section>

  <section class="cards">
    <div class="card left"><div class="card-photo" role="img" aria-label="Photo of a hillside ocean-view home with solar panels"></div></div>
    <div class="card mid">
      <span class="start-mark"></span>
      <div class="start-title">GET STARTED</div>
      <div class="start-link">CLICK HERE TO GET STARTED</div>
    </div>
    <div class="card right"><div class="card-photo" role="img" aria-label="Photo of a hillside ocean-view home with solar panels"></div></div>
  </section>

  <footer class="footer">
    Copyright 2008 Brindle Ray Solar, Fresno, CA. All rights reserved.
    <nav><a href="#">Home</a> | <a href="#">Company</a> | <a href="#">Services</a> | <a href="#">FAQ</a> | <a href="#">Contact Us</a> | <a href="#">Sitemap</a></nav>
  </footer>
</div>
</body>
</html>
```